Optometrist/Eye Care Clinic Business card with new logo attached

We are a small, independent eye care clinic in Canada. We have recently updated our logo (as attached), and would like a professional, modern and health care oriented business card to highlight our office details and our optometrist. We'd like to incorporate the blue colours as seen on our logo.

Target Market(s)

demographic: age 35-65 male/female equal

Industry/Entity Type

Health Care

Contact Information for Business Card

Name of clinic: "Marrow Bend Eye Care Optometry"

Font styles to use
Sans Serif

Colors
0355a3

Requirements
Must have
• our website: marrowbendeyecare.com
• Dr Lena Quorvik
• Optometrist
• 217-392 E Halvering Ave
• Vancouver BC V6R 3J8
• P: 604-319-2058
• E: info@marrowbendeyecare.com
Nice to have
• front side: logo/name of clinic as seen on logo attached and website
• backside: logo on the left side, and name/title/address/phone/email

```html
<!DOCTYPE html>
<html lang="en">
<head>
<meta charset="utf-8">
<title>Marrow Bend Eye Care Optometry – Business Card</title>
<link href="https://fonts.googleapis.com/css2?family=Open+Sans:wght@400;600;700&display=swap" rel="stylesheet">
<style>
  :root {
    --backdrop: #3a3330;
    --card: #0e0e0f;
    --brand-blue: #1a8ccc;
    --deep-blue: #0355a3;
    --text-light: #d6d6d6;
    --text-muted: #9a9a9a;
    --silver: #e4e4e4;
    --divider: #2c2c2e;
  }
  * { box-sizing: border-box; margin: 0; padding: 0; }
  html, body {
    width: 1200px; height: 844px; overflow: hidden;
    background: var(--backdrop);
    font-family: "Open Sans", Arial, sans-serif;
  }
  .stage {
    position: relative; width: 1200px; height: 844px;
    display: flex; align-items: center; justify-content: center; gap: 40px;
  }
  .card {
    width: 540px; height: 309px;
    background: var(--card);
    border-radius: 3px;
    box-shadow: 0 12px 30px rgba(0,0,0,.45);
    position: relative;
  }

  /* Back side: clinic mark + contact details */
  .card-back { display: flex; }
  .mark-zone {
    width: 46%;
    display: flex; flex-direction: column; align-items: center; justify-content: center; gap: 16px;
    border-right: 1px solid var(--divider);
  }
  .mark-dot {
    width: 92px; height: 92px; border-radius: 50%;
    background: var(--deep-blue);
  }
  .mark-name {
    color: var(--brand-blue);
    font-weight: 600; font-size: 14px;
    text-align: center; line-height: 1.35;
  }
  .details {
    flex: 1; padding: 42px 0 0 26px;
    color: var(--text-light); font-size: 15px; line-height: 1.35;
  }
  .doctor-name {
    color: var(--brand-blue); font-weight: 700; font-size: 19px; text-transform: uppercase;
  }
  .doctor-title { margin-bottom: 14px; }
  .address { margin-bottom: 14px; }
  .contact-list { list-style: none; }
  .contact-list li { display: flex; align-items: center; gap: 8px; }
  .contact-list svg { width: 12px; height: 12px; flex: none; fill: var(--brand-blue); }

  /* Front side: clinic name + website */
  .card-front {
    display: flex; flex-direction: column; align-items: center; justify-content: center; gap: 34px;
  }
  .clinic-lockup { display: flex; align-items: center; gap: 18px; }
  .clinic-dot { width: 70px; height: 70px; border-radius: 50%; background: var(--silver); }
  .clinic-name {
    color: var(--silver); font-weight: 400; font-size: 22px;
    letter-spacing: .12em; text-transform: uppercase; line-height: 1.25;
  }
  .website { color: var(--text-muted); font-size: 15px; }
</style>
</head>
<body>
<main class="stage">
  <section class="card card-back" aria-label="Business card back">
    <div class="mark-zone">
      <span class="mark-dot"></span>
      <p class="mark-name">Marrow Bend<br>Eye Care Optometry</p>
    </div>
    <div class="details">
      <h1 class="doctor-name">Dr Lena Quorvik</h1>
      <p class="doctor-title">Optometrist</p>
      <p class="address">217-392 E Halvering Ave<br>Vancouver BC V6R 3J8</p>
      <ul class="contact-list">
        <li><svg viewBox="0 0 12 12" aria-hidden="true"><path d="M2.5 1l2 2.2-1 1.3a7 7 0 0 0 4 4l1.3-1 2.2 2-1.2 1.5C5 10.8 1.2 7 .9 2.2z"/></svg>604-319-2058</li>
        <li><svg viewBox="0 0 12 12" aria-hidden="true"><path d="M0 2.5h12v7H0z M0 2.5l6 4 6-4" stroke="#0e0e0f" stroke-width=".8"/></svg>info@marrowbendeyecare.com</li>
        <li><svg viewBox="0 0 12 12" aria-hidden="true"><circle cx="6" cy="6" r="6"/><path d="M0 6h12M6 0c-3 3-3 9 0 12M6 0c3 3 3 9 0 12" stroke="#0e0e0f" stroke-width=".8" fill="none"/></svg>www.marrowbendeyecare.com</li>
      </ul>
    </div>
  </section>

  <section class="card card-front" aria-label="Business card front">
    <div class="clinic-lockup">
      <span class="clinic-dot"></span>
      <p class="clinic-name">Marrow Bend<br>Eye Care<br>Optometry</p>
    </div>
    <p class="website">www.marrowbendeyecare.com</p>
  </section>
</main>
</body>
</html>
```